Business Card Design for Kind Helper

I am starting my own consultancy business, using what I learned in marketing and advertising to help Non -profits with marketing and communications needs. I need a professional business card design to hand out to my clients.

My business name is “Outreach2Kindness” my vision is that this need this to be reflective of marketing doing good for the world through the power of communications. I like the color palettes in olives, creams and oranges but am open to design options.
In addition to the cards I am asking for separate file for the logo and will need a JPG, PSD Vector File.

Information to go on the card:

Morwenna Calloway
Marketing Consultant
Email: outreach2kindness@mailbrook.com, callowaym1@brinmoreu.edu
Website: Outreach2Kindness.com

Communications

```html
<!DOCTYPE html>
<html lang="en">
<head>
<meta charset="utf-8">
<title>Outreach2Kindness – Business Card Options</title>
<link href="https://fonts.googleapis.com/css2?family=PT+Sans:wght@400;700&family=PT+Sans+Narrow:wght@700&display=swap" rel="stylesheet">
<style>
  :root {
    --ink: #231f20;
    --gold: #e9b332;
    --gold-pale: #f6e2ae;
    --paper: #ffffff;
  }
  * { margin: 0; padding: 0; box-sizing: border-box; }
  html, body {
    width: 1200px;
    height: 705px;
    overflow: hidden;
    background: var(--paper);
  }
  .sheet {
    position: relative;
    width: 1200px;
    height: 705px;
    background: var(--paper);
    font-family: "PT Sans", Arial, sans-serif;
    color: var(--ink);
  }
  .card {
    position: absolute;
    width: 540px;
    height: 330px;
    overflow: hidden;
  }
  .card--plain { left: 0; top: 0; }
  .card--circle { left: 541px; top: 0; }
  .card--raised { left: 0; top: 348px; }
  .card--faint { left: 541px; top: 348px; }

  .card__brand {
    position: absolute;
    left: 28px;
    top: 54px;
    font-size: 33px;
    font-weight: 400;
    letter-spacing: -0.2px;
    white-space: nowrap;
    z-index: 2;
  }
  .card__person {
    position: absolute;
    left: 31px;
    top: 100px;
    font-family: "PT Sans Narrow", "Arial Narrow", sans-serif;
    font-weight: 700;
    font-size: 19px;
    line-height: 25px;
    z-index: 2;
  }
  .card__contact {
    position: absolute;
    left: 11px;
    top: 283px;
    font-family: "PT Sans Narrow", "Arial Narrow", sans-serif;
    font-weight: 700;
    font-size: 17.5px;
    line-height: 22px;
    white-space: nowrap;
    z-index: 2;
  }

  /* Logo stand-in: one plain circle with the name set beneath it */
  .mark {
    position: absolute;
    display: flex;
    flex-direction: column;
    align-items: center;
    gap: 12px;
    z-index: 1;
  }
  .mark__dot {
    display: block;
    border-radius: 50%;
    background: var(--gold);
  }
  .mark__name {
    font-family: "PT Sans", Arial, sans-serif;
    font-weight: 700;
    font-size: 19px;
    color: var(--gold);
    white-space: nowrap;
  }

  .card--plain .mark { left: 343px; top: 36px; width: 180px; }
  .card--plain .mark__dot { width: 140px; height: 140px; }

  .card--circle .backdrop {
    position: absolute; left: 250px; top: 25px; width: 288px; height: 278px; z-index: 0;
  }
  .card--circle .mark { left: 350px; top: 72px; width: 180px; }
  .card--circle .mark__dot { width: 118px; height: 118px; background: var(--paper); }
  .card--circle .mark__name { color: var(--paper); }

  .card--raised .mark { left: 345px; top: 34px; width: 180px; }
  .card--raised .mark__dot { width: 150px; height: 150px; }

  .card--faint .mark { left: 335px; top: 92px; width: 180px; }
  .card--faint .mark__dot { width: 130px; height: 130px; background: var(--gold-pale); }
  .card--faint .mark__name { color: var(--gold-pale); }
</style>
</head>
<body>
<main class="sheet">

  <section class="card card--plain">
    <div class="mark"><span class="mark__dot"></span><span class="mark__name">Outreach2Kindness</span></div>
    <h1 class="card__brand">Outreach2Kindness</h1>
    <p class="card__person">Morwenna Calloway<br>Marketing Consultant</p>
    <p class="card__contact">Email: outreach2kindness@mailbrook.com, callowaym1@brinmoreu.edu<br>Website: Outreach2Kindness.com</p>
  </section>

  <section class="card card--circle">
    <svg class="backdrop" viewBox="0 0 288 278" aria-hidden="true">
      <circle cx="188" cy="131" r="187" fill="#e9b332"/>
    </svg>
    <div class="mark"><span class="mark__dot"></span><span class="mark__name">Outreach2Kindness</span></div>
    <h2 class="card__brand">Outreach2Kindness</h2>
    <p class="card__person">Morwenna Calloway<br>Marketing Consultant</p>
    <p class="card__contact">Email: outreach2kindness@mailbrook.com, callowaym1@brinmoreu.edu<br>Website: Outreach2Kindness.com</p>
  </section>

  <section class="card card--raised">
    <div class="mark"><span class="mark__dot"></span><span class="mark__name">Outreach2Kindness</span></div>
    <h2 class="card__brand">Outreach2Kindness</h2>
    <p class="card__person">Morwenna Calloway<br>Marketing Consultant</p>
    <p class="card__contact">Email: outreach2kindness@mailbrook.com, callowaym1@brinmoreu.edu<br>Website: Outreach2Kindness.com</p>
  </section>

  <section class="card card--faint">
    <div class="mark"><span class="mark__dot"></span><span class="mark__name">Outreach2Kindness</span></div>
    <h2 class="card__brand">Outreach2Kindness</h2>
    <p class="card__person">Morwenna Calloway<br>Marketing Consultant</p>
    <p class="card__contact">Email: outreach2kindness@mailbrook.com, callowaym1@brinmoreu.edu<br>Website: Outreach2Kindness.com</p>
  </section>

</main>
</body>
</html>
```